Talvenridge

We are re-branding the company with a new logo (attached) which I would
like to go on one side of the card, and I have attached a file showing what
the old back side looked like, and I do like the characters that show the
phone, e-mails, etc., I don't like the current arrangement, and I want
something clean, clear and out of the box, as we are an aviation consulting
firm, and we work outside of the box.

```html
<!DOCTYPE html>
<html lang="en">
<head>
<meta charset="utf-8">
<title>Talvenridge Business Card</title>
<link href="https://fonts.googleapis.com/css2?family=Lato:wght@400;700;900&display=swap" rel="stylesheet">
<style>
  :root {
    --bg: #3a3a3c;
    --brand-red: #b0101c;
    --brand-red-dark: #8e0c16;
    --card-white: #f6f6f6;
    --ink: #2b2b2b;
    --ink-soft: #6d6d6d;
    --on-red: #f4dcdc;
  }
  * { margin: 0; padding: 0; box-sizing: border-box; }
  html, body { width: 1200px; height: 900px; overflow: hidden; }
  body {
    background: var(--bg);
    font-family: "Lato", Arial, sans-serif;
    position: relative;
  }
  .card {
    position: absolute;
    left: 250px;
    width: 700px;
    height: 400px;
    border-radius: 4px;
    overflow: hidden;
  }
  .card-front { top: 40px; background: var(--brand-red); color: #fff; }
  .card-back { top: 460px; background: var(--card-white); color: var(--ink); }

  .brand {
    display: flex;
    align-items: center;
    gap: 14px;
  }
  .brand-dot {
    width: 34px; height: 34px; border-radius: 50%;
  }
  .brand-name {
    font-weight: 900;
    font-size: 54px;
    letter-spacing: 3px;
    text-transform: uppercase;
    line-height: 1;
  }
  .tagline {
    font-size: 17px;
    letter-spacing: 1px;
    margin-top: 6px;
  }

  .card-front .brand-block { position: absolute; left: 70px; top: 90px; }
  .card-front .brand-dot { background: #fff; }
  .card-front .brand-name { color: #fff; }
  .card-front .tagline { color: var(--on-red); margin-left: 48px; }
  .services {
    position: absolute; left: 118px; top: 260px;
    font-size: 21px; font-weight: 700; line-height: 1.6;
    color: var(--on-red);
  }

  .card-back .brand-block { position: absolute; left: 150px; top: 50px; }
  .card-back .brand-dot { background: var(--brand-red); }
  .card-back .brand-name { color: var(--brand-red); font-size: 48px; }
  .card-back .tagline { color: var(--ink-soft); margin-left: 48px; }

  .person {
    position: absolute; right: 40px; top: 150px; text-align: right;
  }
  .person-name { color: var(--brand-red); font-weight: 900; font-size: 30px; letter-spacing: 1px; }
  .person-title { color: var(--ink); font-size: 18px; letter-spacing: 2px; margin-top: 2px; }

  .icon-tab {
    position: absolute; left: 0; top: 250px;
    width: 70px; height: 150px;
    background: var(--brand-red);
    border-top-right-radius: 12px;
    display: flex; flex-direction: column; align-items: center;
    padding-top: 16px; gap: 16px;
  }
  .icon-tab svg { width: 28px; height: 28px; }
  .contacts {
    position: absolute; left: 100px; top: 258px;
    list-style: none; font-size: 22px; font-weight: 700; color: var(--ink);
    line-height: 1.9;
  }
  .address {
    position: absolute; right: 40px; top: 270px;
    font-size: 22px; font-weight: 700; color: var(--ink);
    text-align: right; line-height: 1.5;
  }
</style>
</head>
<body>
  <section class="card card-front">
    <div class="brand-block">
      <div class="brand">
        <span class="brand-dot"></span>
        <span class="brand-name">Talvenridge</span>
      </div>
      <p class="tagline">trusted experience • proven solutions</p>
    </div>
    <p class="services">Aircraft Finances &amp; Leasing / Technical Services<br>Aviation consulting / Airline restructuring</p>
  </section>

  <section class="card card-back">
    <div class="brand-block">
      <div class="brand">
        <span class="brand-dot"></span>
        <span class="brand-name">Talvenridge</span>
      </div>
      <p class="tagline">trusted experience • proven solutions</p>
    </div>

    <div class="person">
      <p class="person-name">YOUR NAME</p>
      <p class="person-title">DESIGNATION</p>
    </div>

    <div class="icon-tab">
      <svg viewBox="0 0 24 24" fill="none" stroke="#fff" stroke-width="1.6" aria-label="Phone">
        <rect x="5" y="2" width="14" height="20" rx="2"/><line x1="10" y1="18.5" x2="14" y2="18.5"/>
      </svg>
      <svg viewBox="0 0 24 24" fill="none" stroke="#fff" stroke-width="1.6" aria-label="Email">
        <rect x="2" y="5" width="20" height="14" rx="1"/><polyline points="2,5 12,13 22,5"/>
      </svg>
      <svg viewBox="0 0 24 24" fill="none" stroke="#fff" stroke-width="1.6" aria-label="Website">
        <circle cx="12" cy="12" r="9"/><line x1="3" y1="12" x2="21" y2="12"/><ellipse cx="12" cy="12" rx="4" ry="9"/>
      </svg>
    </div>
    <ul class="contacts">
      <li>0400 518 276</li>
      <li>mk@talvenridge.aero</li>
      <li>www.talvenridge.aero</li>
    </ul>
    <p class="address">14 Larkspur Way<br>Fenwick, CA 90412</p>
  </section>
</body>
</html>
```